Pelvin Advisory Business Card Design

Business card for business consulting company, using attached logo. We do financial and strategic consulting, and want a clean, professional image with a bit of fun. Our logo is a flat whale tail, which symbolizes the Orca whale, a highly collaborative, group based animal that is very successful in navigating the ocean, protecting the herd, and hunting. We like the logo that is blue and gray on white one one side, but would be open to a blue card with white lettering on the other side... or whatever you'd suggest
Updates
Hi all - I have had the logo modified to take the shadowing off the tail. I will post it on the brief... under a file name called updated logo. thank you Added Saturday, April 25, 2015
Target Market(s)
Small to medium sized businesses ($10M to $500M in revenue per year), financial and sales executives, general managers, attorneys and CPAs
Industry/Entity Type
Financial
Contact Information for Business Card
Want company name, contact info - name, title, telephone, email, website, linkedin, twitter and Facebook. No physical address yet.
Requirements
Must have
- contemporary design, bold, strong, confident but with a bit of fun. prominently feature the logo and the whale tail icon
Nice to have
- unique touches that would differentiate us from a regular card... for example, logo and writing all on front on white background, but on back - logo in white on a blue background
- open to idea of different shapes of card than standard... but not sure

```html
<!DOCTYPE html>
<html lang="en">
<head>
<meta charset="utf-8">
<title>Pelvin Advisory Business Card</title>
<link href="https://fonts.googleapis.com/css2?family=Open+Sans:wght@300;400;600;700&display=swap" rel="stylesheet">
<style>
  :root {
    --navy: #1f4a8c;
    --navy-deep: #173a72;
    --paper: #fbfbfb;
    --ink-gray: #a9adb3;
    --stage: #e7e8ea;
    --white: #ffffff;
  }
  * { margin: 0; padding: 0; box-sizing: border-box; }
  html, body { width: 1200px; height: 885px; overflow: hidden; }
  body {
    background: var(--stage);
    font-family: "Open Sans", Arial, sans-serif;
    position: relative;
  }
  .card {
    position: absolute;
    width: 620px;
    height: 354px;
    border-radius: 4px;
    overflow: hidden;
    box-shadow: 0 10px 28px rgba(0,0,0,0.18);
  }
  /* Front */
  .card-front { left: 60px; top: 60px; background: var(--navy); }
  .front-top {
    position: absolute; left: 0; top: 0; width: 100%; height: 160px;
    background: var(--paper);
  }
  .brand {
    position: absolute; left: 36px; top: 46px;
    display: flex; align-items: center; gap: 16px;
  }
  .brand-square {
    width: 64px; height: 64px; border-radius: 8px; background: var(--navy);
  }
  .brand-name {
    font-weight: 600; font-size: 50px; line-height: 1; color: var(--navy);
    letter-spacing: -1.5px;
  }
  .tagline {
    position: absolute; right: 40px; top: 116px;
    font-weight: 400; font-size: 15px; color: var(--navy);
  }
  .front-bottom {
    position: absolute; left: 0; top: 160px; width: 100%; height: 194px;
    color: var(--white);
  }
  .person { position: absolute; left: 36px; top: 40px; }
  .person-name { font-weight: 700; font-size: 24px; line-height: 1.1; }
  .person-phone { font-size: 16px; margin-top: 2px; }
  .person-address { font-size: 15px; margin-top: 24px; line-height: 1.35; }
  .divider {
    position: absolute; left: 290px; top: 36px; width: 1px; height: 122px;
    background: rgba(255,255,255,0.7);
  }
  .contact-list {
    position: absolute; left: 312px; top: 34px; list-style: none;
    font-size: 15px; line-height: 25px;
  }
  .contact-list li { display: flex; align-items: center; gap: 10px; }
  .contact-list svg { flex: none; }

  /* Back */
  .card-back { left: 520px; top: 470px; background: var(--navy); }
  .back-band {
    position: absolute; left: 0; top: 104px; width: 100%; height: 146px;
    background: var(--paper);
  }
  .back-brand {
    position: absolute; left: 40px; top: 30px;
    display: flex; align-items: center; gap: 16px;
  }
  .back-tagline {
    position: absolute; right: 40px; top: 104px;
    font-size: 15px; color: var(--navy);
  }
</style>
</head>
<body>

<section class="card card-front" aria-label="Business card front">
  <div class="front-top">
    <div class="brand">
      <div class="brand-square"></div>
      <span class="brand-name">pelvinadvisory</span>
    </div>
    <span class="tagline">business consulting</span>
  </div>
  <div class="front-bottom">
    <div class="person">
      <p class="person-name">Dana Whitlock</p>
      <p class="person-phone">+1.555.014.2290</p>
      <p class="person-address">418 Larkspur Lane Ferndale<br>MI 49000 US</p>
    </div>
    <div class="divider"></div>
    <ul class="contact-list">
      <li><svg width="14" height="14" viewBox="0 0 14 14"><circle cx="7" cy="7" r="6" fill="none" stroke="#fff" stroke-width="1.4"/><path d="M1 7h12M7 1c-3 3-3 9 0 12M7 1c3 3 3 9 0 12" fill="none" stroke="#fff" stroke-width="1"/></svg>www.pelvinadvisory.com</li>
      <li><svg width="14" height="14" viewBox="0 0 14 14"><rect x="1" y="3" width="12" height="8" fill="none" stroke="#fff" stroke-width="1.4"/><path d="M1 3l6 5 6-5" fill="none" stroke="#fff" stroke-width="1.2"/></svg>dwhitlock@pelvinadvisory.com</li>
      <li><svg width="14" height="14" viewBox="0 0 14 14"><rect x="1" y="1" width="12" height="12" rx="2" fill="#fff"/></svg>pelvinadvisory</li>
      <li><svg width="14" height="14" viewBox="0 0 14 14"><rect x="1" y="1" width="12" height="12" rx="2" fill="#fff"/></svg>social.link/pelvinadvisory</li>
      <li><svg width="14" height="14" viewBox="0 0 14 14"><rect x="1" y="1" width="12" height="12" rx="2" fill="#fff"/></svg>pelvinadvisory</li>
    </ul>
  </div>
</section>

<section class="card card-back" aria-label="Business card back">
  <div class="back-band">
    <div class="back-brand">
      <div class="brand-square"></div>
      <span class="brand-name">pelvinadvisory</span>
    </div>
    <span class="back-tagline">business consulting</span>
  </div>
</section>

</body>
</html>
```